Business Card for Marriage Commissioner

I am a marriage commissioner in the province of Alberta, meaning that I perform civil unions here. I have been trying to think of a unique design for my business card, something a bit different. A lot of "unique" designs seem to incorporate unique cuts or "some assembly required" or printed on plastic or meat. I would like my design to be a full colour card that is a typical business card size.

The information on the card should have:
Lon Varbeck
my occupation: Marriage Commissioner
my website: www.lonvarbeck.ca
my e-mail: lon@lonvarbeck.ca
my phone: 780-914-2086

I originally submitted a design to the printer that had a screen capture of a finduro search window, with my name and occupation in the text box. And underneath that, my phone number. Nothing else. They indicated they could not print this because it was a copyright violation.

One option on the design is I am a retired chemist-so a chemistry themed card would also be of interest, as long as it isn't a "Quiet Reagent" theme, as I have that on my other business cards already...

I would prefer a single sided card, but I am open to a double sided card if it is clever!

I would also prefer not to have pictures of male and female couples as in my position I will also marry same sex couples. Same thing for male/female symbols. Someone has submitted two graduated cylinders in love, which is very clever, and gets around this male/female type.

Thanks for your help and interest.

Target Market(s)

Young couples.

Industry/Entity Type

Plastic

Requirements
Nice to have
• chemistry ideas!
Should not have
• Male/female pictures, male/female symbols.
No QR codes.
No transparent designs, will go on paper stock.

```html
<!DOCTYPE html>
<html lang="en">
<head>
<meta charset="utf-8">
<title>Lon Varbeck — Marriage Commissioner</title>
<link rel="stylesheet" href="https://fonts.googleapis.com/css2?family=Marcellus&display=swap">
<style>
  :root {
    --page: #ffffff;
    --card-dark: #262523;
    --card-gold: #e6d594;
    --text-gold: #c8b26f;
    --seal-gold: #e8d898;
    --ribbon-teal: #5bc4d0;
    --ribbon-text: #ffffff;
    --stitch: #cfcab8;
  }
  html, body {
    margin: 0;
    padding: 0;
    width: 1200px;
    height: 1200px;
    overflow: hidden;
    background: var(--page);
  }
  .canvas {
    position: relative;
    width: 1200px;
    height: 1200px;
  }
  .business-card {
    position: absolute;
    left: 327px;
    top: 70px;
    width: 546px;
    height: 958px;
    border-radius: 30px;
    overflow: hidden;
    background: var(--card-dark);
    font-family: "Marcellus", "Times New Roman", serif;
  }
  .header-band {
    position: absolute;
    left: 0; top: 0;
    width: 100%;
    height: 146px;
    border-bottom: 3px solid var(--card-gold);
  }
  .website {
    position: absolute;
    left: 0; right: 0;
    top: 90px;
    text-align: center;
    color: var(--text-gold);
    font-size: 26px;
    letter-spacing: 0.5px;
    line-height: 1;
  }
  .gold-field {
    position: absolute;
    left: 0;
    top: 152px;
    width: 100%;
    height: 653px;
    background: var(--card-gold);
  }
  .footer-rule {
    position: absolute;
    left: 0;
    top: 808px;
    width: 100%;
    height: 3px;
    background: var(--card-gold);
  }
  .seal {
    position: absolute;
    left: 79px;
    top: 285px;
    width: 388px;
    height: 388px;
  }
  .seal-name {
    position: absolute;
    left: 0; right: 0;
    top: 154px;
    text-align: center;
    color: var(--seal-gold);
    font-size: 44px;
    line-height: 1;
    letter-spacing: 0.5px;
  }
  .seal-title {
    position: absolute;
    left: 0; right: 0;
    top: 211px;
    text-align: center;
    color: var(--seal-gold);
    font-size: 20px;
    line-height: 1;
    letter-spacing: 0.3px;
  }
  .contact-ribbon {
    position: absolute;
    left: 58px;
    top: 842px;
    width: 430px;
    height: 80px;
  }
  .contact-email {
    position: absolute;
    left: 0; right: 0;
    top: 14px;
    text-align: center;
    color: var(--ribbon-text);
    font-size: 26px;
    line-height: 1;
  }
  .contact-phone {
    position: absolute;
    left: 0; right: 0;
    top: 51px;
    text-align: center;
    color: var(--ribbon-text);
    font-size: 18px;
    line-height: 1;
  }
</style>
</head>
<body>
<div class="canvas">
  <div class="business-card">
    <div class="header-band">
      <div class="website">WWW.LONVARBECK.CA</div>
    </div>

    <div class="gold-field"></div>
    <div class="footer-rule"></div>

    <div class="seal">
      <svg width="388" height="388" viewBox="0 0 388 388">
        <circle cx="194" cy="194" r="194" fill="var(--card-dark)"/>
        <circle cx="194" cy="194" r="183" fill="none" stroke="var(--stitch)" stroke-width="1.2" stroke-dasharray="5 4"/>
        <rect x="108" y="85" width="172" height="44" rx="22" fill="var(--seal-gold)" opacity="0.85"
              role="img" aria-label="Gold leaf flourish ornament above the name"/>
        <rect x="108" y="254" width="172" height="44" rx="22" fill="var(--seal-gold)" opacity="0.85"
              role="img" aria-label="Gold leaf flourish ornament below the title"/>
      </svg>
      <div class="seal-name">LON VARBECK</div>
      <div class="seal-title">MARRIAGE COMMISSIONER</div>
    </div>

    <div class="contact-ribbon">
      <svg width="430" height="80" viewBox="0 0 430 80">
        <path d="M30 0 H400 Q412 26 430 40 Q412 54 400 80 H30 Q18 54 0 40 Q18 26 30 0 Z" fill="var(--ribbon-teal)"/>
      </svg>
      <div class="contact-email">LON@LONVARBECK.CA</div>
      <div class="contact-phone">780-914-2086</div>
    </div>
  </div>
</div>
</body>
</html>
```